Vocational Mentor needs an impressive business card

1. I need a business card (or maybe three with identic look) to promote me and my three business titles/services:
- Vocational Mentor. I help people find their vocation and live happily from it. I use my 20 years of experience in business, management and psychology to help them identify the most efficient ways to make a living doing what they are passionate about.
- Business Angel. I help founders start a succesful business with minimum risks and costs. I use my 20 years of experience in sales, management and entrepreneurship to help them identify the most efficient ways, in terms of time and cost, to validate their business idea.
- Learning Designer. I design unique learning programs that produce long-term cognitive and behavioural changes to people and organisations. I use my 20 years of experience in learning, teaching and change management to create minimalist experiences and processes that allow them to change efficiently in their pursued direction.

2. I would like a two-sided business card, on the front with my name, contact details and titles, on the back the explanation of the services.
Updates

Hi all,

I updated my brief, included contacts info and give feedback on all designs I got. I am new on this platform so please tell me if you need anything else or if I don't use corectly the platform forms.

Kind regards,
Tudor

Hi all,

I shortened the services description by deleting the phrase "I call..."

Kind regards,
Tudor

Target Market(s)

Freelancers, startups, people and organization willing to invest in change through ultimate learning experiences

Industry/Entity Type

Business

Font styles to use
Serif

Requirements
Must have
• Front side: full name, titles, web site, email, phone like below:
Tudor Vasilache
Vocational Mentor, Business Angel, Learning Designer
info@tudorvasilache.example
www.tudorvasilache.example
+40-745-TUDORV
Nice to have
• Back side: the description of the services I provide as in the task description.
1/3: it would be nice if I can jam all three titles on the front side but then I need a solution to jam all three services on the back side.

```html
<!DOCTYPE html>
<html lang="en">
<head>
<meta charset="utf-8">
<title>Tudor Vasilache — Business Card</title>
<link rel="stylesheet" href="https://fonts.googleapis.com/css2?family=Open+Sans:wght@300;400;700&family=PT+Sans:wght@700&display=swap">
<style>
  :root {
    --backdrop: #a8958d;
    --card: #141414;
    --card-edge: #0c0c0c;
    --name: #2a2d2f;
    --name-glow: #8a9aa0;
    --title: #7d8c93;
    --contact: #6f8088;
    --icon: #5f747d;
    --heading: #5cc3e4;
    --body: #6d7f87;
    --swirl: rgba(90, 130, 135, 0.45);
  }
  html, body {
    margin: 0;
    padding: 0;
    width: 1200px;
    height: 750px;
    overflow: hidden;
    background: var(--backdrop);
  }
  .stage {
    position: relative;
    width: 1200px;
    height: 750px;
  }
  .card {
    position: absolute;
    width: 532px;
    height: 318px;
    background: var(--card);
    box-shadow: 0 0 0 1px var(--card-edge);
    overflow: hidden;
  }
  .card--front { left: 55px; top: 150px; }
  .card--back  { left: 620px; top: 296px; }

  .swirl {
    position: absolute;
    border-radius: 50%;
    filter: blur(6px);
  }
  .card--front .swirl {
    left: 60px; top: 40px;
    width: 420px; height: 230px;
    background: radial-gradient(ellipse at 50% 55%, var(--swirl) 0%, rgba(60, 95, 100, 0.18) 45%, transparent 72%);
    transform: rotate(-24deg);
  }
  .card--back .swirl {
    left: -20px; top: 0;
    width: 110px; height: 318px;
    background: radial-gradient(ellipse at 50% 40%, rgba(90, 130, 135, 0.25) 0%, transparent 70%);
  }

  .front__name {
    position: absolute;
    left: 0; right: 0; top: 70px;
    margin: 0;
    text-align: center;
    font-family: "PT Sans", sans-serif;
    font-weight: 700;
    font-size: 21px;
    letter-spacing: 0.5px;
    color: var(--name);
    text-shadow: 0 0 1px var(--name-glow), 0 0 2px var(--name-glow);
  }
  .front__titles {
    position: absolute;
    left: 0; right: 0; top: 113px;
    margin: 0;
    padding: 0;
    list-style: none;
    text-align: center;
    font-family: "Open Sans", sans-serif;
    font-weight: 300;
    font-size: 14.5px;
    line-height: 18px;
    color: var(--title);
  }
  .front__contacts {
    position: absolute;
    left: 205px; top: 199px;
    margin: 0;
    padding: 0;
    list-style: none;
    font-family: "Open Sans", sans-serif;
    font-weight: 300;
    font-size: 13px;
    line-height: 16px;
    color: var(--contact);
  }
  .contact {
    display: flex;
    align-items: center;
    gap: 6px;
  }
  .contact__icon {
    width: 10px;
    height: 10px;
    flex: none;
    fill: none;
    stroke: var(--icon);
    stroke-width: 1.2;
  }

  .services {
    position: absolute;
    left: 50px; top: 48px;
    width: 442px;
    font-family: "Open Sans", sans-serif;
  }
  .service + .service { margin-top: 16px; }
  .service__title {
    margin: 0 0 4px;
    font-weight: 700;
    font-size: 10.5px;
    color: var(--heading);
  }
  .service__text {
    margin: 0;
    font-weight: 400;
    font-size: 9.2px;
    line-height: 10.8px;
    color: var(--body);
  }
</style>
</head>
<body>
<main class="stage">

  <section class="card card--front" aria-label="Business card front">
    <div class="swirl" role="img" aria-label="Soft teal smoke swirl decoration"></div>
    <h1 class="front__name">Tudor Vasilache</h1>
    <ul class="front__titles">
      <li>Vocational Mentor</li>
      <li>Business Angel</li>
      <li>Learning Designer</li>
    </ul>
    <ul class="front__contacts">
      <li class="contact">
        <svg class="contact__icon" viewBox="0 0 10 10" aria-hidden="true"><rect x="0.6" y="2" width="8.8" height="6.2"/><path d="M0.6 2 L5 5.6 L9.4 2"/></svg>
        <span>info@tudorvasilache.example</span>
      </li>
      <li class="contact">
        <svg class="contact__icon" viewBox="0 0 10 10" aria-hidden="true"><circle cx="5" cy="5" r="4.2"/><path d="M0.8 5 H9.2 M5 0.8 C2.8 3 2.8 7 5 9.2 M5 0.8 C7.2 3 7.2 7 5 9.2"/></svg>
        <span>www.tudorvasilache.example</span>
      </li>
      <li class="contact">
        <svg class="contact__icon" viewBox="0 0 10 10" aria-hidden="true"><path d="M2 1 L3.8 1 L4.4 3.2 L3.3 4.1 C3.9 5.4 4.7 6.2 6 6.8 L6.9 5.7 L9 6.3 L9 8 C5 8.6 1.4 5 2 1 Z"/></svg>
        <span>+40-745-TUDORV</span>
      </li>
    </ul>
  </section>

  <section class="card card--back" aria-label="Business card back">
    <div class="swirl" role="img" aria-label="Faint teal smoke swirl decoration"></div>
    <div class="services">
      <article class="service">
        <h2 class="service__title">Vocational Mentor</h2>
        <p class="service__text">I help people to find their vocation and live happily from it. I use my 20 years of experience in business, management and psychology to help them identify the most efficient ways to make a living doing what they are passionate about. I call this service vocational mentoring.</p>
      </article>
      <article class="service">
        <h2 class="service__title">Business Angel</h2>
        <p class="service__text">I help founders to start a succesful business with minimum risks and costs. I use my 20 years of experience in sales, management and entrepreneurship to help them identify the most efficient ways, in terms of time and cost, to validate their business idea. I call this service lean-startup mentoring.</p>
      </article>
      <article class="service">
        <h2 class="service__title">Learning Designer</h2>
        <p class="service__text">I design unique learning programs that produce long-term cognitive and behavioural changes to people and organisations. I use my 20 years of experience in learning, teaching and change management to create minimalist experiences and processes that allows them to change efficiently in their pursued direction. I call this service ultimate learning design.</p>
      </article>
    </div>
  </section>

</main>
</body>
</html>
```